Construction APP

We need to design a modern app IOS/Android where my team can create a profile with their info, (maybe share some pictures), reviews, submit time cards, show their availability, etc.

Like a taxi app but for construction. We also want to be able to assign each team member to a project manager with who they currently working. So we will also need to be able to create profiles at the Administration level.

The goal is to keep innovating the app as we grow, so we are always open to suggestions and ideas.

Low design quality

Industry/Entity Type

Construction

Colors
FFC000
F8CF3A
FAE287
FDF2CF
FEFAEE

Requirements
Must have
• IOS/Android APP where my team can create a profile with their info, (maybe share some pictures), reviews, submit time cards, show their availability, etc.We also want to be able to assign each team member to a project manager with who they currently working. So we will also need to be able to create profiles at the Administration level.

```html
<!DOCTYPE html>
<html lang="en">
<head>
<meta charset="utf-8">
<title>Construction App – Login, Sign up, Confirm</title>
<link href="https://fonts.googleapis.com/css2?family=Inter:wght@400;500;600;700&display=swap" rel="stylesheet">
<style>
  :root {
    --bg: #f4f4f4;
    --card: #ffffff;
    --ink: #1d1d1f;
    --muted: #9a9a9a;
    --field: #fafafa;
    --rule: #8a8a8a;
    --accent: #ffc000;
    --box-border: #ececec;
  }
  * { box-sizing: border-box; margin: 0; padding: 0; }
  html, body { width: 1200px; height: 1000px; overflow: hidden; }
  body { background: var(--bg); font-family: "Inter", sans-serif; color: var(--ink); position: relative; }

  .screen {
    position: absolute; top: 113px; width: 356px; height: 774px;
    background: var(--card); border-radius: 22px;
    box-shadow: 0 18px 40px rgba(40, 60, 90, 0.10);
  }
  .screen--login { left: 28px; }
  .screen--signup { left: 422px; }
  .screen--confirm { left: 816px; }

  .status-time { position: absolute; left: 20px; top: 12px; font-size: 14px; font-weight: 600; line-height: 18px; }
  .status-icons { position: absolute; right: 14px; top: 15px; width: 68px; height: 12px; }

  .screen-title { position: absolute; font-size: 30px; font-weight: 700; line-height: 36px; }
  .field-label { position: absolute; left: 16px; font-size: 13px; line-height: 16px; }

  .field { position: absolute; left: 16px; width: 324px; height: 56px; background: var(--field); }
  .field::after { content: ""; position: absolute; left: 8px; right: 8px; bottom: 8px; height: 2px; background: var(--rule); }
  .field-placeholder { position: absolute; left: 8px; top: 16px; font-size: 17px; line-height: 22px; color: var(--muted); }
  .field-dots { position: absolute; left: 8px; top: 23px; display: flex; gap: 8.5px; }
  .field-dots span { width: 8px; height: 8px; border-radius: 50%; background: var(--ink); }
  .field-icon { position: absolute; right: 10px; top: 16px; width: 24px; height: 24px; }

  .text-link { position: absolute; right: 16px; font-size: 13px; line-height: 16px; }

  .primary-button {
    position: absolute; left: 40px; width: 276px; height: 56px; background: var(--accent);
    border-radius: 2px; font-size: 19px; font-weight: 600; line-height: 56px; text-align: center;
  }
  .account-switch { position: absolute; left: 0; right: 0; top: 686px; text-align: center; font-size: 16px; line-height: 20px; }
  .account-switch a { color: var(--ink); font-weight: 500; text-decoration: underline; }

  .home-indicator { position: absolute; left: 121px; top: 763px; width: 115px; height: 4px; border-radius: 2px; background: var(--ink); }

  .confirm-heading { position: absolute; left: 23px; top: 194px; font-size: 16px; font-weight: 600; line-height: 20px; }
  .confirm-text { position: absolute; left: 23px; top: 236px; width: 312px; font-size: 17px; line-height: 21px; }
  .code-title { position: absolute; left: 0; right: 0; top: 359px; text-align: center; font-size: 18px; font-weight: 600; line-height: 22px; }
  .code-boxes { position: absolute; left: 16px; top: 432px; display: flex; gap: 11px; }
  .code-box { position: relative; width: 56px; height: 62px; background: var(--field); border: 1px solid var(--box-border); }
  .code-box::after { content: ""; position: absolute; left: 16px; width: 24px; bottom: 8px; height: 1.5px; background: var(--ink); }
</style>
</head>
<body>

<svg width="0" height="0" style="position:absolute">
  <defs>
    <symbol id="status" viewBox="0 0 68 12">
      <rect x="0" y="8" width="3" height="4" rx="0.8" fill="#1d1d1f"/>
      <rect x="4.5" y="6" width="3" height="6" rx="0.8" fill="#1d1d1f"/>
      <rect x="9" y="3.5" width="3" height="8.5" rx="0.8" fill="#1d1d1f"/>
      <rect x="13.5" y="1" width="3" height="11" rx="0.8" fill="#1d1d1f"/>
      <path d="M23 4.2a10 10 0 0 1 14 0l-1.5 1.5a8 8 0 0 0-11 0zM25.5 6.8a6.3 6.3 0 0 1 9 0l-1.5 1.5a4.2 4.2 0 0 0-6 0zM28 9.4a2.8 2.8 0 0 1 4 0L30 11.5z" fill="#1d1d1f"/>
      <rect x="43" y="0.5" width="22" height="11" rx="3" fill="none" stroke="#1d1d1f" stroke-opacity="0.4"/>
      <rect x="45" y="2.5" width="18" height="7" rx="1.6" fill="#1d1d1f"/>
      <path d="M66.5 4v4a2 2 0 0 0 0-4z" fill="#1d1d1f" fill-opacity="0.4"/>
    </symbol>
    <symbol id="icon-mail" viewBox="0 0 24 24">
      <rect x="2" y="4" width="20" height="16" rx="4" fill="none" stroke="#ffc000" stroke-width="1.6"/>
      <path d="M6.5 9l5.5 4 5.5-4" fill="none" stroke="#ffc000" stroke-width="1.6" stroke-linecap="round" stroke-linejoin="round"/>
    </symbol>
    <symbol id="icon-eye-off" viewBox="0 0 24 24">
      <path d="M2 12s3.6-6.5 10-6.5S22 12 22 12s-3.6 6.5-10 6.5S2 12 2 12z" fill="none" stroke="#ffc000" stroke-width="1.6"/>
      <circle cx="12" cy="12" r="3.2" fill="none" stroke="#ffc000" stroke-width="1.6"/>
      <path d="M4 21L21 3" stroke="#ffc000" stroke-width="1.6" stroke-linecap="round"/>
    </symbol>
    <symbol id="icon-user" viewBox="0 0 24 24">
      <circle cx="12" cy="7" r="4" fill="none" stroke="#ffc000" stroke-width="1.6"/>
      <rect x="5" y="14" width="14" height="8" rx="4" fill="none" stroke="#ffc000" stroke-width="1.6"/>
    </symbol>
    <symbol id="icon-phone" viewBox="0 0 24 24">
      <path d="M5 3.5h3.2l1.6 4-2.1 1.4a11 11 0 0 0 6.4 6.4l1.4-2.1 4 1.6v3.2A2 2 0 0 1 17.5 20 15 15 0 0 1 3 5.5 2 2 0 0 1 5 3.5z" fill="none" stroke="#ffc000" stroke-width="1.6" stroke-linejoin="round"/>
    </symbol>
  </defs>
</svg>

<section class="screen screen--login">
  <div class="status-time">9:41</div>
  <svg class="status-icons"><use href="#status"/></svg>
  <h1 class="screen-title" style="left:17px; top:119px;">Login</h1>

  <label class="field-label" style="top:247px;">E-mail</label>
  <div class="field" style="top:271px;">
    <span class="field-placeholder">Example@email.com</span>
    <svg class="field-icon"><use href="#icon-mail"/></svg>
  </div>

  <label class="field-label" style="top:375px;">Password</label>
  <div class="field" style="top:399px;">
    <div class="field-dots"><span></span><span></span><span></span><span></span><span></span><span></span><span></span><span></span></div>
    <svg class="field-icon"><use href="#icon-eye-off"/></svg>
  </div>

  <span class="text-link" style="top:475px;">Forgot Password?</span>
  <div class="primary-button" style="top:555px;">Log in</div>
  <p class="account-switch">Need an account? <a>Sign up</a></p>
  <div class="home-indicator"></div>
</section>

<section class="screen screen--signup">
  <div class="status-time">9:41</div>
  <svg class="status-icons"><use href="#status"/></svg>
  <h1 class="screen-title" style="left:25px; top:63px;">Sign up</h1>

  <label class="field-label" style="top:167px;">Name- Surname</label>
  <div class="field" style="top:191px;">
    <span class="field-placeholder">Name Surname</span>
    <svg class="field-icon"><use href="#icon-user"/></svg>
  </div>

  <label class="field-label" style="top:295px;">E-mail</label>
  <div class="field" style="top:319px;">
    <span class="field-placeholder">E-mail address</span>
    <svg class="field-icon"><use href="#icon-mail"/></svg>
  </div>

  <label class="field-label" style="top:423px;">Phone</label>
  <div class="field" style="top:447px;">
    <span class="field-placeholder">Phone number</span>
    <svg class="field-icon"><use href="#icon-phone"/></svg>
  </div>

  <div class="primary-button" style="top:567px;">Sign up</div>
  <p class="account-switch">Just already an account? <a>Log in</a></p>
  <div class="home-indicator"></div>
</section>

<section class="screen screen--confirm">
  <div class="status-time">9:41</div>
  <svg class="status-icons"><use href="#status"/></svg>

  <h2 class="confirm-heading">Confirm your registration</h2>
  <p class="confirm-text">We have sent you a numeric code via SMS: Enter the code to confirm your registration</p>

  <h3 class="code-title">Enter the numeric code</h3>
  <div class="code-boxes">
    <div class="code-box"></div><div class="code-box"></div><div class="code-box"></div><div class="code-box"></div><div class="code-box"></div>
  </div>

  <span class="text-link" style="top:516px;">Resend code?</span>
  <div class="primary-button" style="top:627px;">Confirm</div>
  <div class="home-indicator"></div>
</section>

</body>
</html>
```